Book Cover

Book cover for a study guide on Galatians. The title would be: "Unbound Hearts: Called Out to Walk Open" Possibly using a bird breaking free from a cage.+

Target Market(s)

We will sell them to our church.

Requirements
Must have
• Authors are Dr. Martin Oskerby and Dr. Helen Oskerby

```html
<!DOCTYPE html>
<html lang="en">
<head>
<meta charset="utf-8">
<title>Unbound Hearts: Called Out to Walk Open — Book Cover Spread</title>
<link rel="stylesheet" href="https://fonts.googleapis.com/css2?family=Anton&family=Arimo:wght@400&family=Open+Sans:wdth,wght@75..100,300..800&display=swap">
<style>
  :root {
    --cover-red: #b93324;
    --cage-red: #9e2a1d;
    --ink: #141414;
    --paper: #ffffff;
    --backdrop: #e6e6e6;
    --fold-line: rgba(0, 0, 0, 0.14);
  }
  html, body {
    margin: 0;
    padding: 0;
    width: 681px;
    height: 1200px;
    overflow: hidden;
    background: var(--backdrop);
  }
  .cover-spread {
    position: absolute;
    left: 0;
    top: 340px;
    width: 1456px;
    height: 1110px;
    transform-origin: 0 0;
    transform: scale(0.46772);
    display: flex;
  }

  /* Back cover */
  .back-cover {
    position: relative;
    width: 691px;
    height: 1110px;
    background: var(--paper);
    border-top: 1px solid var(--cover-red);
    box-sizing: border-box;
  }
  .back-blurb {
    position: absolute;
    left: 70px;
    top: 84px;
    width: 560px;
    font-family: "Arimo", "Arial", sans-serif;
    font-size: 16.2px;
    line-height: 21.3px;
    color: var(--ink);
  }
  .back-blurb p {
    margin: 0 0 21.3px;
  }
  .back-authors {
    position: absolute;
    left: 490px;
    top: 990px;
    margin: 0;
    font-family: "Open Sans", "Arial", sans-serif;
    font-stretch: 80%;
    font-size: 18px;
    line-height: 21.5px;
    color: var(--ink);
  }

  /* Shared author name styling */
  .author-name { display: block; white-space: nowrap; }
  .author-name .honorific { font-weight: 600; }
  .author-name .given { font-weight: 800; }
  .author-name .family { font-weight: 400; }

  /* Spine */
  .spine {
    position: relative;
    width: 67px;
    height: 1110px;
    background: var(--cover-red);
  }
  .spine-title {
    position: absolute;
    left: 15px;
    top: 79px;
    margin: 0;
    writing-mode: vertical-rl;
    font-family: "Open Sans", "Arial", sans-serif;
    font-weight: 600;
    font-size: 25px;
    line-height: 36px;
    letter-spacing: 0.12em;
    color: var(--paper);
    white-space: nowrap;
    text-transform: uppercase;
  }
  .spine-authors {
    position: absolute;
    left: 14px;
    top: 892px;
    margin: 0;
    writing-mode: vertical-rl;
    font-family: "Open Sans", "Arial", sans-serif;
    font-stretch: 80%;
    font-size: 17px;
    line-height: 20px;
    color: var(--paper);
  }

  /* Front cover */
  .front-cover {
    position: relative;
    width: 698px;
    height: 1110px;
    background: var(--cover-red);
    border-left: 1px solid var(--fold-line);
    box-sizing: border-box;
    overflow: hidden;
  }
  .cover-illustration {
    position: absolute;
    left: 62px;
    top: 79px;
    width: 480px;
    height: 825px;
    display: block;
  }
  .series-title {
    position: absolute;
    left: 62px;
    top: 904px;
    transform-origin: 0 0;
    transform: rotate(-90deg);
    margin: 0;
    font-family: "Anton", "Impact", sans-serif;
    font-weight: 400;
    font-size: 104px;
    line-height: 1;
    color: var(--ink);
    white-space: nowrap;
  }
  .main-title {
    position: absolute;
    right: 41px;
    top: 164px;
    margin: 0;
    font-family: "Open Sans", "Arial", sans-serif;
    font-weight: 800;
    font-stretch: 80%;
    font-size: 165px;
    line-height: 148px;
    letter-spacing: -0.035em;
    color: var(--paper);
    text-align: right;
    text-transform: uppercase;
  }
  .main-title span { display: block; }
  .author-line {
    position: absolute;
    left: 0;
    right: 0;
    top: 1015px;
    margin: 0;
    font-family: "Open Sans", "Arial", sans-serif;
    font-weight: 300;
    font-size: 17px;
    letter-spacing: 0.2em;
    color: var(--paper);
    text-align: center;
    white-space: nowrap;
  }
  .author-line strong { font-weight: 700; }
</style>
</head>
<body>
  <main class="cover-spread">
    <section class="back-cover">
      <div class="back-blurb">
        <p>Lorem Ipsum is simply dummy text of the printing and typesetting industry. Lorem Ipsum has been the industry's standard dummy text ever since the 1500s, when an unknown printer took a galley of type and scrambled it to make a type specimen book. It has survived not only five centuries, but also the leap into electronic typesetting, remaining essentially unchanged. It was popularised in the 1960s with the release of Transferline sheets containing Lorem Ipsum passages, and more recently with desktop publishing software like Pagewright Studio including versions of Lorem Ipsum.</p>
        <p>Lorem Ipsum is simply dummy text of the printing and typesetting industry. Lorem Ipsum has been the industry's standard dummy text ever since the 1500s, when an unknown printer took a galley of type and scrambled it to make a type specimen book. It has survived not only five centuries, but also the leap into electronic typesetting, remaining essentially unchanged. It was popularised in the 1960s with the release of Transferline sheets containing Lorem Ipsum passages, and more recently with desktop publishing software like Pagewright Studio including versions of Lorem Ipsum.</p>
        <p>Lorem Ipsum is simply dummy text of the printing and typesetting industry. Lorem Ipsum has been the industry's standard dummy text ever since the 1500s, when an unknown printer took a galley of type and scrambled it to make a type specimen book. It has survived not only five centuries, but also the leap into electronic typesetting, remaining essentially unchanged. It was popularised in the 1960s with the release of Transferline sheets containing Lorem Ipsum passages, and more recently with desktop publishing software like Pagewright Studio including versions of Lorem Ipsum.</p>
        <p>Lorem Ipsum is simply dummy text of the printing and typesetting industry. Lorem Ipsum has been the industry's standard dummy text ever since the 1500s, when an unknown printer took a galley of type and scrambled it to make a type specimen book. It has survived not only five centuries, but also the leap into electronic typesetting, remaining essentially unchanged. It was popularised in the 1960s with the release of Transferline sheets containing Lorem Ipsum passages, and more recently with desktop publishing software like Pagewright Studio including versions of Lorem Ipsum.</p>
      </div>
      <p class="back-authors">
        <span class="author-name"><span class="honorific">Dr.</span> <span class="given">Martin</span> <span class="family">Oskerby</span></span>
        <span class="author-name"><span class="honorific">Dr.</span> <span class="given">Helen</span> <span class="family">Oskerby</span></span>
      </p>
    </section>

    <section class="spine">
      <p class="spine-title">Unbound Hearts: Called Out To Walk Open</p>
      <p class="spine-authors">
        <span class="author-name"><span class="honorific">Dr.</span> <span class="given">Martin</span> <span class="family">Oskerby</span></span>
        <span class="author-name"><span class="honorific">Dr.</span> <span class="given">Helen</span> <span class="family">Oskerby</span></span>
      </p>
    </section>

    <section class="front-cover">
      <svg class="cover-illustration" role="img" aria-label="Illustration of an open hanging birdcage with a bird flying free out of it" viewBox="0 0 480 825" preserveAspectRatio="none">
        <rect x="0" y="0" width="480" height="825" fill="var(--cage-red)"/>
      </svg>

      <h1 class="series-title">UNBOUND HEARTS:</h1>

      <h2 class="main-title">
        <span>Called</span>
        <span>Out</span>
        <span>To</span>
        <span>Walk</span>
        <span>Open</span>
      </h2>

      <p class="author-line">Authors are Dr. Martin Oskerby <strong>and</strong> Dr. Helen Oskerby</p>
    </section>
  </main>
</body>
</html>
```